Whitcombe Legal Group Promo Flyers

** I've increased the payment for this job is hopes of getting some more sophisticated design options. See feedback on current designs for guidance. I want this to be sophisticated, elegant, effective design. Please stay away from the brown/blue color palate that has been used in so many of these design options. It's not working. I'd love to see richer, deeper colors with more dimension. **

The Whitcombe Legal Group is trying to market itself as a law firm that is different than other firms. They listen to clients, meet their guidelines, provide excellent communication and will even start work for free to showcase their expertise. I need three separate flyers that will primarily be used as PDFs, but may on occasion be printed.

We're looking for a clean look.

I've attached two sample infographics that are pieces done by another company in the industry. We like that look (sizes of those are different, but the overall look is good).

Target Market(s)

Insurance companies and corporate executives who buy legal services to help them manage their book of litigation. Typical buyer is in 40s to 50s. Fairly racially diverse.

Industry/Entity Type

Communication

Requirements
Must have
• Each document will be a one-page PDF that can be easily emailed to potential clients. Must be one side only for each.

One flyer each for these three files, which are included:
Whitcombe firm by the numbers
Whitcombe firm client advantage program
Whitc firm overview

Must use firm logo. Contact information should pop.

"Topping the list" piece is an inforgraphic that should really focus on bold use of the numbers or text in blue. Mix up the page and make it fun and interesting.

Logo colors are:

Brown: R: 101 G: 50 B:27, HEX: 65321B

Grey: R:129 G: 145 B:144, HEX: 819190
Nice to have
• Firm website is very dull and uninteresting. These pieces need to pop more than past pieces.

http://www.whitcombelegalgroup-example.com/
Should not have
• No stock photos of people in groups (all law firms use those and they are boring and overdone).

```html
<!DOCTYPE html>
<html lang="en">
<head>
<meta charset="utf-8">
<title>Whitcombe Legal Group – Client Partner Plan Flyer</title>
<link rel="stylesheet" href="https://fonts.googleapis.com/css2?family=Montserrat:wght@600;700&family=Open+Sans:wght@400;600;700&display=swap">
<style>
  :root{
    --bg:#e4e2e6;
    --red:#d52a35;
    --red-deep:#b51f2a;
    --red-panel:#a81b26;
    --red-soft:#e2525b;
    --red-pale:#ef8b90;
    --white:#ffffff;
    --ink:#4a4a4a;
    --dark:#1e1e1e;
    --grey:#819190;
    --photo-light:#e9e3de;
    --photo-mid:#b99d88;
    --photo-dark:#6f3a22;
  }
  *{box-sizing:border-box;margin:0;padding:0}
  html,body{width:1200px;height:750px;overflow:hidden}
  body{background:var(--bg);font-family:'Open Sans',Arial,sans-serif;position:relative}

  .flyer{position:absolute;left:350px;top:22px;width:500px;height:706px;background:var(--red);overflow:hidden;box-shadow:0 6px 22px rgba(0,0,0,.18)}

  .hero-photo{position:absolute;left:0;top:0;width:500px;height:390px;
    background:linear-gradient(135deg,var(--photo-dark) 0%,var(--photo-mid) 28%,var(--photo-light) 55%,#f4efea 100%)}

  .firm-name-box{position:absolute;right:20px;top:0;width:138px;height:84px;background:var(--white);padding:14px 12px 0 14px}
  .firm-name{font-family:'Open Sans',Arial,sans-serif;font-weight:400;color:var(--grey);font-size:17px;line-height:1.08}

  .stairs{position:absolute;left:0;top:260px;width:500px;height:140px}

  .plan-disc{position:absolute;left:252px;top:176px;width:214px;height:214px;border-radius:50%;background:var(--white);
    box-shadow:0 3px 10px rgba(0,0,0,.25);display:flex;align-items:center;justify-content:center;text-align:center}
  .plan-title{font-family:'Montserrat',Arial,sans-serif;font-weight:700;color:var(--dark);line-height:1.12}
  .plan-title .plan-main{display:block;font-size:31px;letter-spacing:.5px}
  .plan-title .plan-sub{display:block;font-size:20px;margin-top:2px}

  .benefits-panel{position:absolute;left:333px;top:392px;width:148px;height:262px;background:var(--red-panel)}

  .headline{position:absolute;left:20px;top:400px;width:300px;color:var(--white);padding-left:10px;border-left:2px solid var(--white)}
  .headline h2{font-family:'Montserrat',Arial,sans-serif;font-weight:600;font-size:19px;line-height:1.1}
  .headline p{font-family:'Montserrat',Arial,sans-serif;font-weight:700;font-size:9.6px;margin-top:3px;letter-spacing:.1px}

  .body-col{position:absolute;top:454px;width:146px;color:var(--white);font-size:8px;line-height:1.26;text-align:justify}
  .body-col.first{left:26px}
  .body-col.second{left:180px}

  .benefits{position:absolute;left:338px;top:408px;width:140px;color:var(--white)}
  .benefits h3{font-family:'Montserrat',Arial,sans-serif;font-weight:600;font-size:13px;margin:0 0 3px 6px}
  .benefits ul{list-style:none}
  .benefits li{position:relative;padding-left:10px;font-size:7.3px;line-height:1.22;margin-bottom:6px}
  .benefits li::before{content:"";position:absolute;left:1px;top:2px;width:5px;height:5px;border-radius:50%;background:var(--white)}

  .contact-bar{position:absolute;left:20px;top:660px;width:462px;height:36px;background:var(--white);display:flex;align-items:center}
  .contact-name{width:50px;margin-left:6px;font-size:7.2px;line-height:1.05;color:var(--grey)}
  .contact-firm{padding-left:8px;border-left:1px solid #ccc;height:28px;display:flex;flex-direction:column;justify-content:center;flex:1;white-space:nowrap}
  .contact-firm strong{font-family:'Montserrat',Arial,sans-serif;font-size:9px;color:#222}
  .contact-firm span{font-size:5.6px;color:var(--ink);margin-top:1px}
  .contact-phone{font-family:'Montserrat',Arial,sans-serif;font-weight:700;font-size:8px;color:#222;padding:0 8px;border-left:1px solid #ccc;height:28px;display:flex;align-items:center;white-space:nowrap}
</style>
</head>
<body>
  <article class="flyer">
    <div class="hero-photo" role="img" aria-label="Photo of a wooden gavel resting on open law books with red leather-bound volumes behind"></div>

    <div class="firm-name-box"><div class="firm-name">The Whitcombe Legal Group</div></div>

    <svg class="stairs" viewBox="0 0 500 140" aria-hidden="true">
      <polygon fill="var(--red-pale)" points="0,80 60,80 60,66 110,66 110,52 160,52 160,38 210,38 210,24 260,24 260,140 0,140"/>
      <polygon fill="var(--red-soft)" points="0,104 70,104 70,92 130,92 130,80 190,80 190,68 250,68 250,56 500,56 500,140 0,140"/>
      <polygon fill="var(--red)" points="0,128 90,128 90,118 160,118 160,108 240,108 240,98 500,98 500,140 0,140"/>
    </svg>

    <div class="benefits-panel"></div>

    <div class="plan-disc">
      <h1 class="plan-title"><span class="plan-main">THE CPP</span><span class="plan-sub">‘CLIENT<br>PARTNER<br>PLAN’</span></h1>
    </div>

    <header class="headline">
      <h2>We’ll begin to work for FREE</h2>
      <p>WE BELIEVE IN TRUE PARTNERSHIPS AND TO PROVE IT</p>
    </header>

    <p class="body-col first">When we say we will work for free, we mean it. We will invest in your business and help you accomplish your goals. At no cost, we will review and analyze select components of your litigation program, including a targeted review of individual files. As part of our review, we’ll work with you to delineate your goals and outline a strategy for success. We complete all of this work at no cost to you because our ultimate goal is to form a partnership that is successful for you and for us. Then it’s on to phase two where we implement the strategy. While working on the cases you assign to</p>

    <p class="body-col second">us, we continuously measure our results and provide you with data so we can hold ourselves accountable to those established benchmarks. On the cases we are handling for you, where possible we will identify opportunities to credit, offset and decrease both litigation fees and expenses. Better than that, we can take program (or file) responsibility off your desk, identify income and cut expense. Let us do the heavy lifting. With this team approach, we can share program and file experience that cuts resolution time, saves legal spend and cuts costs year over year.</p>

    <section class="benefits">
      <h3>Benefits of CPP</h3>
      <ul>
        <li>Attorneys focused on winning your case and accomplishing your goals rather than logging hours – legal services focused on results.</li>
        <li>Certainty about the ultimate cost of your legal spend.</li>
        <li>Litigation management metrics. We’re comfortable being measured on our performance and will integrate your culture and process into reporting categories such as case inventories, time (speed of resolution), cost (both outcome and expense), quality (based on agreed goals from stakeholders) and predictability (anticipated versus actual, budget and outcome).</li>
        <li>Proof of concept from experienced administration of national, regional and local programs</li>
      </ul>
    </section>

    <footer class="contact-bar">
      <div class="contact-name">The Whitcombe Legal Group</div>
      <div class="contact-firm">
        <strong>The Whitcombe Legal Group</strong>
        <span>48 W. Harlow Ave. Suite 1200 Chicago, Illinois 60610, United States.</span>
      </div>
      <div class="contact-phone">Phone : (555) 014 2288 &nbsp;|&nbsp; Fax : (555) 014 2291</div>
    </footer>
  </article>
</body>
</html>
```